Professional and Modern Company Letterhead for Fintech Startup

Brisk Lending is a fintech startup that provides home financing.

Our company requires letterhead in Microsoft word format. Colors must come from our ADA compliant doc.

Company logo, equal housing opportunity logo, and legal language must be included somewhere on the document.

We'd love an option that maximizes space on the page for text vs have design take up the entire thing.

Target Market(s)

Partners, clients, and employees

Industry/Entity Type

Finance

Font styles to use
Sans Serif

Requirements
Must have
• Must use company colors that are ADA compliant (see attachment). Must include logo in a prominent position. Must include equal housing opportunity logo and legal info at the bottom:

©Brisk Lending LLC. NMLS #2739054 | 4172 Harrow Lane #204, Boulder, CO 80305 | Not available in all states | 800.437.5820 | help@brisklending.example
Nice to have
• Something modern and clean.

```html
<!DOCTYPE html>
<html lang="en">
<head>
<meta charset="utf-8">
<title>Brisk Lending — Letterhead</title>
<link rel="stylesheet" href="https://fonts.googleapis.com/css2?family=Montserrat:wght@300;400;500;700&family=Arimo:wght@400&display=swap">
<style>
  :root {
    --stage: #a9c6e2;
    --paper: #ffffff;
    --brand-teal: #37bcd4;
    --brand-yellow: #f2d21b;
    --ink-dark: #333333;
    --ink-body: #8c8c8c;
    --ink-soft: #9a9a9a;
    --ink-footer: #7d7d7d;
    --rule: #8a8a8a;
  }
  * { box-sizing: border-box; margin: 0; padding: 0; }
  html, body {
    width: 1200px; height: 1200px; overflow: hidden;
    background: var(--stage);
    font-family: "Montserrat", sans-serif;
  }
  .letterhead {
    position: absolute; left: 190px; top: 20px;
    width: 821px; height: 1160px;
    background: var(--paper);
  }
  .brand {
    position: absolute; left: 0; right: 0; top: 46px;
    display: flex; justify-content: center; align-items: center; gap: 10px;
  }
  .brand-mark { width: 20px; height: 20px; background: var(--brand-yellow); }
  .brand-name {
    font-family: "Montserrat", sans-serif; font-weight: 700;
    font-size: 40px; letter-spacing: -0.5px; color: var(--brand-teal);
  }
  .recipient { position: absolute; left: 84px; top: 266px; }
  .recipient-label {
    font-weight: 500; font-size: 14px; letter-spacing: 2.5px; color: var(--ink-dark);
  }
  .recipient-name {
    margin-top: 8px; font-weight: 500; font-size: 13.5px; color: var(--brand-teal);
  }
  .recipient-address {
    margin-top: 5px; font-weight: 300; font-size: 11px; line-height: 18px; color: var(--ink-soft);
  }
  .letter-date {
    position: absolute; right: 83px; top: 267px;
    font-weight: 400; font-size: 11.5px; color: var(--ink-dark);
  }
  .letter-body {
    position: absolute; left: 84px; top: 422px; width: 654px;
    font-weight: 300; font-size: 11.5px; line-height: 14.5px;
    color: var(--ink-body); text-align: justify;
  }
  .letter-body p + p { margin-top: 14.5px; }
  .sign-off { position: absolute; left: 84px; top: 822px; }
  .signature {
    width: 140px; height: 32px; border-radius: 3px;
    background: linear-gradient(90deg, #ececec, #f6f6f6);
  }
  .signer-name {
    margin-top: 17px; font-weight: 500; font-size: 13.5px; letter-spacing: 0.3px; color: var(--ink-dark);
  }
  .signer-title { font-weight: 300; font-size: 10.5px; color: var(--ink-soft); margin-top: 2px; margin-left: -2px; }
  .footer {
    position: absolute; left: 0; right: 0; top: 1086px; height: 44px;
    font-family: "Arimo", sans-serif; font-size: 13.5px; line-height: 18px; color: var(--ink-footer);
  }
  .footer-col { position: absolute; top: 0; height: 44px; display: flex; flex-direction: column; justify-content: center; }
  .footer-contact { left: 93px; }
  .contact-line { display: flex; align-items: center; gap: 6px; }
  .contact-line svg { width: 12px; height: 12px; fill: var(--brand-teal); }
  .footer-address { left: 310px; }
  .footer-license { left: 514px; justify-content: flex-end; padding-bottom: 5px; }
  .footer-rule { position: absolute; top: 4px; width: 1.5px; height: 38px; background: var(--rule); }
  .rule-one { left: 277px; } .rule-two { left: 482px; } .rule-three { left: 647px; }
  .housing-badge { position: absolute; left: 677px; top: 0; width: 48px; height: 44px; }
</style>
</head>
<body>
  <main class="letterhead">
    <header class="brand">
      <span class="brand-mark"></span>
      <span class="brand-name">Brisk Lending</span>
    </header>

    <section class="recipient">
      <div class="recipient-label">TO</div>
      <div class="recipient-name">Daniel Okafor</div>
      <div class="recipient-address">
        Human Resources<br>
        Northfield Systems Inc.<br>
        2218-B Alder Court, Westbrook<br>
        W42 USA
      </div>
    </section>
    <div class="letter-date">Friday, 01/01/2018</div>

    <section class="letter-body">
      <p>Lorem ipsum dolor sit amet, consectetuer adipiscing elit, sed diam nonmmy nibh euismod tincidunt ut laoreet dolore magna aliquam erat volutpat. Ut wisi enim ad minim veniam, quis nostrud exerci tationmcorper suscipit lobortis nisl ut aliquip ex ea commodo consequat. Duis autem vel eum iriure dolor in hendrerit in vulputate velit esse molestie consequat, vel illum dolore eu feugiat nulla facilisis at vero eros et accumsan et iusto odio dignissim qui blandit praesent luptatum zzril delenit augue duis dolore te feugait nulla facilisi.</p>
      <p>Nam liber tempor cum soluta nobis eleifend option congue nihil imprdiet doming id quod mazim placerat facer possim assum. Typi non habent claritatem insitam;</p>
      <p>Est usus legentis in iis qui facit eorum claritatem.</p>
      <p>Investigationes demonstraverunt lectores legere me lius quod ii legunt saepius. Claritas est etiam processus dynamicus, qui sequitur mutationem consuetudium lectorum. Mirum est notare quam littera gothica, quam nunc putamus parum claram, anteposuerit litterarum formas humanitatis per seacula quarta decima et quinta decima. Eodem modo typi, qui nunc nobis videntur parum clari, fiant sollemnes in futurum.</p>
      <p>consectetuer adipiscing elit, sed diam nonummy nibh euismod tincidunt ut laoreet dolore magna aliquam erat volutpat. Ut wisi enim ad minim veniam, quis nostrud exerci tation ullamcorper suscipit lobortis nisl ut aliquip ex ea commodo consequat. Duis autem vel eum iriure dolor in hendrerit in vulputate velit esse molestie consequat, vel illum dolore eu feugiat nulla facilisis at vero eros et accumsan et iusto odio dignissim qui blandit praesent luptatum zzril delenit augue duis dolore te feugait nulla facilisi.</p>
      <p>Nam liber tempor cum soluta nobis eleifend option congue nihil imperdiet .</p>
    </section>

    <section class="sign-off">
      <div class="signature" role="img" aria-label="Handwritten signature of Evan Mercer"></div>
      <div class="signer-name">Evan Mercer</div>
      <div class="signer-title">Managing Director</div>
    </section>

    <footer class="footer">
      <div class="footer-col footer-contact">
        <div class="contact-line">
          <svg viewBox="0 0 24 24" aria-hidden="true"><path d="M6.6 10.8a15.2 15.2 0 0 0 6.6 6.6l2.2-2.2a1 1 0 0 1 1-.25 11.4 11.4 0 0 0 3.6.57 1 1 0 0 1 1 1V20a1 1 0 0 1-1 1A17 17 0 0 1 3 4a1 1 0 0 1 1-1h3.5a1 1 0 0 1 1 1c0 1.25.2 2.45.57 3.6a1 1 0 0 1-.25 1z"/></svg>
          <span>800.437.5820</span>
        </div>
        <div class="contact-line">
          <svg viewBox="0 0 24 24" aria-hidden="true"><path d="M2 5h20v14H2z M2 5l10 8 10-8" fill="none" stroke="#37bcd4" stroke-width="2.4"/></svg>
          <span>help@brisklending.example</span>
        </div>
      </div>
      <span class="footer-rule rule-one"></span>
      <div class="footer-col footer-address">
        <span>4172 Harrow Lane #204</span>
        <span>Boulder, CO 80305</span>
      </div>
      <span class="footer-rule rule-two"></span>
      <div class="footer-col footer-license"><span>NMLS #2739054</span></div>
      <span class="footer-rule rule-three"></span>
      <svg class="housing-badge" viewBox="0 0 48 44" role="img" aria-label="Equal housing opportunity badge">
        <rect x="6" y="6" width="36" height="32" fill="none" stroke="#222" stroke-width="3"/>
      </svg>
    </footer>
  </main>
</body>
</html>
```